Letterhead for new real estate company in South Africa named Lofthaven

A letterhead with the directors and company details to be editable as these changes often

Target Market(s)

In line with our logo brief and our newly designed logo and corporate fee

Industry/Entity Type

Real Estate

Requirements
Must have
• Details as per the sample letterhead provided.

```html
<!DOCTYPE html>
<html lang="en">
<head>
<meta charset="utf-8">
<title>Lofthaven Letterhead</title>
<link href="https://fonts.googleapis.com/css2?family=Poppins:wght@400&family=Didact+Gothic&display=swap" rel="stylesheet">
<style>
  :root {
    --green: #34b06f;
    --earth: #6d6558;
    --ink: #2b2b2b;
    --body-ink: #3a3a3a;
    --paper-light: #f2f2f2;
    --paper-dark: #e2e2e2;
    --white: #ffffff;
  }
  html, body {
    margin: 0;
    padding: 0;
    width: 960px;
    height: 1200px;
    overflow: hidden;
  }
  .letterhead {
    position: relative;
    width: 960px;
    height: 1200px;
    background: linear-gradient(100deg, var(--paper-light) 0%, var(--paper-dark) 70%, #e6e6e6 100%);
    font-family: "Didact Gothic", "Century Gothic", sans-serif;
    color: var(--body-ink);
    overflow: hidden;
  }
  .brand {
    position: absolute;
    left: 88px;
    top: 100px;
    display: flex;
    align-items: center;
    gap: 14px;
  }
  .brand-dot {
    width: 38px;
    height: 38px;
    border-radius: 50%;
    background: var(--green);
  }
  .brand-name {
    font-family: "Poppins", sans-serif;
    font-weight: 400;
    font-size: 38px;
    color: var(--green);
    letter-spacing: 0.5px;
  }
  .contact {
    position: absolute;
    left: 640px;
    top: 78px;
    font-family: "Poppins", sans-serif;
    font-size: 14.5px;
    line-height: 18.5px;
    color: var(--ink);
    list-style: none;
    margin: 0;
    padding: 0;
  }
  .contact li {
    position: relative;
    padding-left: 21px;
    margin-bottom: 3px;
  }
  .contact li:first-child { margin-bottom: 6px; }
  .contact svg {
    position: absolute;
    left: 0;
    top: 3px;
    width: 12px;
    height: 12px;
    fill: var(--green);
  }
  .salutation {
    position: absolute;
    left: 88px;
    top: 348px;
    margin: 0;
    font-family: "Didact Gothic", sans-serif;
    font-size: 23px;
    color: var(--ink);
    font-weight: 400;
  }
  .letter-body {
    position: absolute;
    left: 88px;
    top: 416px;
    width: 792px;
    font-size: 13.6px;
    line-height: 19px;
    text-align: justify;
  }
  .letter-body p { margin: 0 0 18px; }
  .closing {
    position: absolute;
    left: 88px;
    top: 800px;
    margin: 0;
    font-size: 13.6px;
  }
  .signature {
    position: absolute;
    left: 88px;
    top: 838px;
    width: 130px;
    height: 76px;
    background: linear-gradient(90deg, #d8d8d8, #e4e4e4);
    border-radius: 4px;
  }
  .footer-wave {
    position: absolute;
    left: 0;
    bottom: 0;
    width: 960px;
    height: 96px;
  }
  .footer-url {
    position: absolute;
    left: 100px;
    bottom: 20px;
    font-family: "Poppins", sans-serif;
    font-size: 15px;
    letter-spacing: 1.4px;
    color: var(--white);
  }
</style>
</head>
<body>
<main class="letterhead">
  <header>
    <div class="brand">
      <span class="brand-dot"></span>
      <span class="brand-name">Lofthaven</span>
    </div>
    <ul class="contact">
      <li>
        <svg viewBox="0 0 12 12"><path d="M6 0a4 4 0 0 0-4 4c0 3 4 8 4 8s4-5 4-8a4 4 0 0 0-4-4zm0 5.5A1.5 1.5 0 1 1 6 2.5a1.5 1.5 0 0 1 0 3z"/></svg>
        14 Marula Crescent<br>Stellenbosch, Western Cape 7600
      </li>
      <li>
        <svg viewBox="0 0 12 12"><path d="M2.5 0.5l2 2.5-1.2 1.4c.8 1.7 2.1 3 3.8 3.8L8.5 7l2.5 2-1 2.2C5 11 1 7 0.8 1.5z"/></svg>
        021-480-3172
      </li>
      <li>
        <svg viewBox="0 0 12 12"><path d="M3 1h6v3H3zM1 5h10v5H9V8H3v2H1zM3.5 9h5v2h-5z"/></svg>
        021-480-3190
      </li>
      <li>
        <svg viewBox="0 0 12 12"><path d="M1 3h10v1L6 7 1 4zM1 5l5 3 5-3v4H1z"/></svg>
        info@lofthaven.com
      </li>
    </ul>
  </header>

  <h1 class="salutation">Dear Mr. Carter,</h1>

  <section class="letter-body">
    <p>Lorem ipsum dolor sit amet, consectetur adipiscing elit. Donec orci purus, luctus vitae dignissim eu, iaculis sed purus. Vivamus faucibus, ipsum nec aliquet viverra, leo mauris condimentum ligula, sit amet sagittis enim ligula quis arcu. Nam egestas tortor id nisi porttitor mattis. In tortor ante, ultricies in suscipit a, tempus non massa. Vivamus et auctor mi. Fusce vel massa nulla. Phasellus nec eros mauris, et scelerisque orci.</p>
    <p>Donec malesuada orci vitae nulla accumsan porta a id massa. Quisque accumsan iaculis magna sit amet fringilla. Maecenas consequat, magna eget tincidunt semper, odio nibh rutrum mi, id feugiat ante nisi eu risus. Vestibulum nunc orci, rhoncus a placerat in, ultricies in mi. Cras mattis varius eros, vel fringilla nisi suscipit eget. Quisque scelerisque sagittis nulla at porttitor.</p>
    <p>Sed id augue vitae urna euismod commodo aliquet a quam. Pellentesque arcu velit, cursus et malesuada ut, consequat et diam. Nullam erat sem, rhoncus id ullamcorper vitae, rhoncus et arcu. In ultricies ultricies nulla, ut rutrum nisi iaculis at. Donec eu magna a metus ornare faucibus. Fusce aliquet faucibus ultricies. Morbi semper, est id tincidunt gravida, sem arcu adipiscing lacus, ac bibendum nulla leo eu purus. Quisque nec diam sed risus consectetur a ccumsan quis quis nibh. Vestibulum id purus lorem.</p>
    <p>It is a long established fact that a reader will be distracted by the readable content of a page when looking at its layout. The point of using Lorem Ipsum is that it has a more-or-less normal distribution of letters, as opposed to using 'Content here, content here', making it look like readable English. Many desktop publishing packages</p>
  </section>

  <p class="closing">Sincerely,</p>
  <div class="signature" role="img" aria-label="Handwritten signature of the director"></div>

  <footer>
    <svg class="footer-wave" viewBox="0 0 960 96" preserveAspectRatio="none" aria-hidden="true">
      <path d="M0 50 C 80 14, 160 4, 240 8 C 420 18, 600 78, 800 80 C 880 80, 930 74, 960 66 L960 96 L0 96 Z" fill="var(--green)"/>
      <path d="M0 58 C 80 24, 160 18, 240 22 C 420 32, 600 86, 800 86 C 880 86, 930 80, 960 72 L960 96 L0 96 Z" fill="var(--white)"/>
      <path d="M0 62 C 80 28, 160 22, 240 26 C 420 36, 600 90, 800 90 C 880 90, 930 84, 960 76 L960 96 L0 96 Z" fill="var(--earth)"/>
    </svg>
    <span class="footer-url">www.lofthaven.com</span>
  </footer>
</main>
</body>
</html>
```